I have a basic design of a poster that I want to make look better. The poster is a list of continuing medical education rules.

JRPPS = Joint Registry for Postgraduate Physician Studies This text should be included. You might also want to include "CME". Please use all the existing elements in the file.

I want to sell this poster to CME offices around the US. The poster should be 24 by 36

Reason: I would like to see more designs. I have received less than ten.

Target Market(s)

CME professionals

Industry/Entity Type

Medical

Colors

Designer to choose colors to be used in the design.

Requirements
Must have
• All elements in the file provided. You can also spell out Joint Registry for Postgraduate Physician Studies.

```html
<!DOCTYPE html>
<html lang="en">
<head>
<meta charset="utf-8">
<title>JRPPS Accreditation Criteria</title>
<link rel="stylesheet" href="https://fonts.googleapis.com/css2?family=Anton&family=Oswald:wght@300;500&family=Roboto+Condensed:wght@400;700&display=swap">
<style>
  :root {
    --slate: #4a6577;
    --slate-dark: #3e5667;
    --orange: #f15a29;
    --panel: #dde1e6;
    --paper: #ffffff;
    --ink: #222a30;
    --white: #ffffff;
  }
  * { box-sizing: border-box; margin: 0; padding: 0; }
  html, body { width: 800px; height: 1200px; overflow: hidden; background: var(--paper); }
  .poster { position: relative; width: 800px; height: 1200px; background: var(--paper); font-family: "Roboto Condensed", "Arial Narrow", sans-serif; color: var(--ink); }

  .masthead { position: absolute; left: 0; top: 0; width: 800px; height: 153px; background: var(--slate); }
  .masthead-texture { position: absolute; right: 0; top: 0; width: 290px; height: 110px;
    background: linear-gradient(90deg, rgba(74,101,119,0) 0%, rgba(150,168,182,0.55) 100%); }
  .masthead-title { position: absolute; left: 24px; top: 34px; font-family: "Anton", sans-serif; font-size: 60px; line-height: 1; color: var(--white); letter-spacing: 0.5px; }

  .intro-band { position: absolute; left: 0; top: 153px; width: 800px; height: 129px; background: var(--orange); }
  .section-label { position: absolute; left: 241px; top: 133px; width: 318px; height: 41px; background: var(--paper);
    font-family: "Oswald", sans-serif; font-weight: 300; font-size: 28px; line-height: 41px; text-align: center; color: var(--orange); letter-spacing: 0.5px; }
  .intro-text { position: absolute; left: 40px; top: 182px; width: 720px; font-family: "Roboto Condensed", sans-serif; font-size: 15px; line-height: 1.3; color: var(--white); text-align: center; }

  .row { position: absolute; left: 24px; width: 752px; display: flex; gap: 12px; align-items: stretch; }
  .criterion { position: relative; background: var(--panel); padding: 6px 8px 6px 0; font-size: 11.5px; line-height: 1.45; text-align: justify; }
  .criterion-tag { float: left; margin: -12px 12px 3px 0; padding: 0 9px; height: 25px; background: var(--orange); color: var(--white);
    font-family: "Oswald", sans-serif; font-weight: 500; font-size: 16px; line-height: 25px; white-space: nowrap; }

  .commendation-band { position: absolute; left: 0; top: 941px; width: 800px; height: 56px; background: var(--slate);
    font-family: "Anton", sans-serif; font-size: 32px; line-height: 56px; text-align: center; color: var(--white); letter-spacing: 1px; }
  .row.small .criterion { font-size: 10px; line-height: 1.4; padding: 5px 6px 5px 0; }
  .row.small .criterion-tag { font-size: 12.5px; height: 18px; line-height: 18px; padding: 0 6px; margin: -8px 8px 2px 0; }
  .site-box { background: var(--slate); color: var(--white); display: flex; align-items: center; justify-content: center;
    font-family: "Roboto Condensed", sans-serif; font-size: 17px; }
  .footer-strip { position: absolute; left: 0; top: 1182px; width: 800px; height: 18px; background: var(--orange); }
</style>
</head>
<body>
<div class="poster">
  <header class="masthead">
    <div class="masthead-texture" role="img" aria-label="Decorative block pattern of staggered squares"></div>
    <h1 class="masthead-title">JRPPS ACCREDITATION CRITERIA</h1>
  </header>
  <section class="intro-band">
  </section>
  <h2 class="section-label">ACCREDITATION CRITERIA</h2>
  <p class="intro-text">The Accreditation Criteria are divided into three levels. To achieve Provisional Accreditation, a two year term, providers must comply with Criteria 1, 2, 3, and 7-12. Providers seeking full Accreditation or reaccreditation for a four-year term must comply with Criteria 1-13. To achieve Accreditation with Commendation, a six-year term, providers must comply with all Accreditation Criteria.</p>

  <div class="row" style="top:296px;height:65px;">
    <div class="criterion" style="width:370px;"><span class="criterion-tag">Criterion 1</span>The provider has a CME mission statement that includes expected results articulated in terms of changes in competence, performance, or patient outcomes that will be the result of the program.</div>
    <div class="criterion" style="width:370px;"><span class="criterion-tag">Criterion 2</span>The provider incorporates into CME activities the educational needs (knowledge, competence, or performance) that underlie the professional practice gaps of their own learners.</div>
  </div>

  <div class="row" style="top:386px;height:49px;">
    <div class="criterion" style="width:535px;"><span class="criterion-tag">Criterion 3</span>The provider has a CME mission statement that includes expected results articulated in terms of changes in competence, performance, or patient outcomes that will be the result of the program.</div>
    <div class="criterion" style="width:205px;"><span class="criterion-tag">Criterion 4</span>This criterion has been eliminated effective February 2014.</div>
  </div>

  <div class="row" style="top:456px;height:24px;">
    <div class="criterion" style="width:752px;"><span class="criterion-tag">Criterion 5</span>The provider chooses educational formats for activities/interventions that are appropriate for the setting, objectives, and desired results of the activity.</div>
  </div>

  <div class="row" style="top:503px;height:59px;">
    <div class="criterion" style="width:470px;"><span class="criterion-tag">Criterion 6</span>The provider develops activities/ educational interventions in the context of desirable physician attributes [eg, Academy of Clinical Sciences (ACS) competencies, Graduate Physician Training Board (GPTB) Competencies].</div>
    <div class="criterion" style="width:270px;"><span class="criterion-tag">Criterion 7</span>The provider develops activities/educational interventions independent of commercial interests. (SCS 1, 2, and 6).</div>
  </div>

  <div class="row" style="top:595px;height:46px;">
    <div class="criterion" style="width:511px;"><span class="criterion-tag">Criterion 8</span>The provider appropriately manages commercial support (if applicable, SCS 3 of the JRPPS Standards for Commercial Support<sup>SM</sup>).</div>
    <div class="criterion" style="width:229px;"><span class="criterion-tag">Criterion 9</span>The provider maintains a separation of promotion from education (SCS 4).</div>
  </div>

  <div class="row" style="top:667px;height:56px;">
    <div class="criterion" style="width:319px;"><span class="criterion-tag">Criterion 10</span>The provider actively promotes improvements in health care and NOT proprietary interests of a commercial interest (SCS 5).</div>
    <div class="criterion" style="width:421px;"><span class="criterion-tag">Criterion 11</span>The provider analyzes changes in learners (competence, performance, or patient outcomes) achieved as a result of the overall program's activities/educational interventions.</div>
  </div>

  <div class="row" style="top:756px;height:46px;">
    <div class="criterion" style="width:752px;"><span class="criterion-tag">Criterion 12</span>The provider gathers data or information and conducts a program-based analysis on the degree to which the CME mission of the provider has been met through the conduct of CME activities/educational interventions.</div>
  </div>

  <div class="row" style="top:826px;height:44px;">
    <div class="criterion" style="width:752px;"><span class="criterion-tag">Criterion 13</span>The provider identifies, plans and implements the needed or desired changes in the overall program (eg, planners, teachers, infrastructure, methods, resources, facilities, interventions) that are required to improve on ability to meet the CME mission.</div>
  </div>

  <div class="row" style="top:894px;height:24px;">
    <div class="criterion" style="width:370px;"><span class="criterion-tag">Criterion 14</span>This criterion has been eliminated effective February 2014.</div>
    <div class="criterion" style="width:370px;"><span class="criterion-tag">Criterion 14</span>This criterion has been eliminated effective February 2014.</div>
  </div>

  <h2 class="commendation-band">ACCREDITATION WITH COMMENDATION</h2>

  <div class="row small" style="top:1010px;height:72px;">
    <div class="criterion" style="width:176px;"><span class="criterion-tag">Criterion 16</span>The provider operates in a manner that integrates CME into the process for improving professional practice.</div>
    <div class="criterion" style="width:182px;"><span class="criterion-tag">Criterion 17</span>The provider utilizes non-education strategies to enhance change as an adjunct to its activities/ educational interventions (e.g., reminders, patient feedback).</div>
    <div class="criterion" style="width:182px;"><span class="criterion-tag">Criterion 18</span>The provider identifies factors outside the provider's control that impact on patient outcomes.</div>
    <div class="criterion" style="width:176px;"><span class="criterion-tag">Criterion 19</span>The provider implements educational strategies to remove, overcome or address barriers to physician change.</div>
  </div>

  <div class="row small" style="top:1096px;height:74px;">
    <div class="criterion" style="width:176px;"><span class="criterion-tag">Criterion 20</span>The provider builds bridges with other stakeholders through collaboration and cooperation.</div>
    <div class="criterion" style="width:182px;"><span class="criterion-tag">Criterion 21</span>The provider builds bridges with other stakeholders through collaboration and cooperation.</div>
    <div class="criterion" style="width:182px;"><span class="criterion-tag">Criterion 22</span>The provider is positioned to influence the scope and content of activities/educational interventions.</div>
    <div class="site-box" style="width:176px;">www.jrpps.org</div>
  </div>

  <div class="footer-strip"></div>
</div>
</body>
</html>
```